Pest Control Company needs business card!

Hi there, we need a business card designed for our new Pest Control Company. Ideally this card will be simple, yet feel elegant and high end. We want to use the colours Orange, Black and White. Please see our attached logo for the exact colours.

Business card details:

Phone - 0461 275 804
Name - Gavin Holloway
Email - Info@steadfastverminguard.com.au

We would also like to include the following list with dot points:

SERVICES / INSPECTIONS

Termites, Wood Borers, Ants, Cockroaches, Spiders, Fleas, Mice, Rats, Bed Bugs, & More!

```html
<!DOCTYPE html>
<html lang="en">
<head>
<meta charset="utf-8">
<title>Steadfast Vermin Guard – Business Card</title>
<link rel="stylesheet" href="https://fonts.googleapis.com/css2?family=Outfit:wght@400;700&family=Roboto+Condensed:wght@700&family=Open+Sans:wght@300&family=Source+Sans+3:wght@600&display=swap">
<style>
  :root {
    --backdrop: #c4dade;
    --card-dark: #1f1c1d;
    --card-dark-soft: #2a2627;
    --ink: #231f20;
    --orange-light: #fbb916;
    --orange-deep: #f47f20;
    --text-grey: #8a8a8a;
    --text-light: #d9d9d9;
  }
  * { box-sizing: border-box; margin: 0; padding: 0; }
  html, body {
    width: 1200px; height: 800px; overflow: hidden;
    background: var(--backdrop);
  }
  .card {
    position: absolute;
    left: 393px;
    width: 414px;
    height: 237px;
    background: var(--card-dark);
    overflow: hidden;
  }
  .card--front { top: 119px; }
  .card--back { top: 430px; }

  .card__photo {
    position: absolute; inset: 0;
    background: radial-gradient(ellipse at 55% 40%, var(--card-dark-soft) 0%, var(--card-dark) 70%);
  }

  /* Front */
  .brand-plate {
    position: absolute;
    left: 110px; top: 71px;
    width: 196px; height: 88px;
    border-radius: 10px;
    background: linear-gradient(90deg, var(--orange-light) 0%, var(--orange-light) 40%, var(--orange-deep) 100%);
    display: flex; align-items: center; justify-content: center;
  }
  .brand-plate__name {
    font-family: "Outfit", sans-serif;
    font-weight: 700;
    font-size: 17px;
    line-height: 1.05;
    text-transform: uppercase;
    text-align: center;
    color: var(--ink);
  }
  .services {
    position: absolute;
    left: 0; right: 0; top: 201px;
    font-family: "Outfit", sans-serif;
    font-weight: 400;
    font-size: 8px;
    line-height: 12px;
    color: var(--text-light);
    text-align: center;
    word-spacing: 1px;
  }
  .services .sep { margin: 0 4px; }

  /* Back */
  .holder-name {
    position: absolute;
    left: 38px; top: 46px;
    font-family: "Roboto Condensed", sans-serif;
    font-weight: 700;
    font-size: 24px;
    text-transform: uppercase;
    color: var(--text-grey);
    letter-spacing: 0.2px;
  }
  .holder-name__first { color: var(--orange-deep); }

  .brand-mark {
    position: absolute;
    right: 30px; top: 44px;
    font-family: "Outfit", sans-serif;
    font-weight: 700;
    font-size: 10px;
    line-height: 1.1;
    text-transform: uppercase;
    color: var(--orange-deep);
    text-align: left;
  }

  .contact {
    position: absolute;
    display: flex; align-items: center; gap: 8px;
  }
  .contact__icon { flex: none; }
  .contact--phone { left: 43px; top: 101px; }
  .contact--phone .contact__text {
    font-family: "Open Sans", sans-serif;
    font-weight: 300;
    font-size: 12px;
    color: var(--text-light);
  }
  .band {
    position: absolute; left: 0; bottom: 0;
    width: 414px; height: 54px;
  }
  .contact--email { left: 38px; top: 202px; }
  .contact--email .contact__text {
    font-family: "Source Sans 3", sans-serif;
    font-weight: 600;
    font-size: 11px;
    color: var(--ink);
  }
</style>
</head>
<body>

<section class="card card--front">
  <div class="card__photo" role="img" aria-label="Dimmed photograph of a pest control technician at work"></div>
  <div class="brand-plate">
    <span class="brand-plate__name">Steadfast<br>Vermin Guard</span>
  </div>
  <p class="services">
    Termites<span class="sep">|</span>Wood Borers<span class="sep">|</span>Ants<span class="sep">|</span>Cockroaches<span class="sep">|</span>Spiders<br>
    Fleas<span class="sep">|</span>Mice<span class="sep">|</span>Rats<span class="sep">|</span>Bed Bugs &amp; More!
  </p>
</section>

<section class="card card--back">
  <div class="card__photo" role="img" aria-label="Dimmed photograph of a pest control technician spraying"></div>

  <h1 class="holder-name"><span class="holder-name__first">Gavin</span> Holloway</h1>

  <div class="brand-mark">Steadfast<br>Vermin Guard</div>

  <div class="contact contact--phone">
    <svg class="contact__icon" width="10" height="10" viewBox="0 0 10 10" aria-hidden="true">
      <circle cx="5" cy="5" r="5" fill="var(--text-light)"/>
      <path d="M3.3 2.6 L4.2 2.5 L4.6 3.7 L4.1 4.2 Q4.6 5.3 5.8 5.9 L6.3 5.4 L7.5 5.8 L7.4 6.7 Q6.8 7.4 5.6 6.9 Q3.6 6 3 4 Q2.8 3 3.3 2.6 Z" fill="var(--card-dark)"/>
    </svg>
    <span class="contact__text">0461 275 804</span>
  </div>

  <svg class="band" viewBox="0 0 414 54" preserveAspectRatio="none" aria-hidden="true">
    <defs>
      <linearGradient id="bandGradient" x1="0" y1="0" x2="1" y2="0">
        <stop offset="0" stop-color="var(--orange-light)"/>
        <stop offset="0.4" stop-color="var(--orange-light)"/>
        <stop offset="0.82" stop-color="var(--orange-deep)"/>
        <stop offset="1" stop-color="var(--orange-deep)"/>
      </linearGradient>
    </defs>
    <path d="M0 0 H221 Q224 0 226 2 L234 10 Q236 12 239 12 H414 V54 H0 Z" fill="url(#bandGradient)"/>
  </svg>

  <div class="contact contact--email">
    <svg class="contact__icon" width="9" height="9" viewBox="0 0 10 10" aria-hidden="true">
      <circle cx="5" cy="5" r="5" fill="var(--ink)"/>
      <rect x="2.6" y="3.3" width="4.8" height="3.4" fill="none" stroke="var(--orange-light)" stroke-width="0.7"/>
      <path d="M2.6 3.3 L5 5.2 L7.4 3.3" fill="none" stroke="var(--orange-light)" stroke-width="0.7"/>
    </svg>
    <span class="contact__text">Info@steadfastverminguard.com.au</span>
  </div>
</section>

</body>
</html>
```